Home Design company focused on remodel and enhancement of kitchens and bathroorms

I already have a logo designed by ArtHarbor, I now need a design for my business cards.
The company is in the remodeling and enhancement industry for homes, focusing on kitchens and bathrooms, however, we can remodel or enhance every room in a home, an office space, etc.

The company's name is VELMOR HOME DESIGN, LLC

We'll focus on clients in the Rio Grande Valley, Texas. Primarily McAllen, Edinburg, Pharr, Mission, Brownsville and South Padre Island.

The design on the business card should transmit reliability, professionalism anda bit of upscale design.

The logo is in black and white, and would like to keep it that way.

The information that needs to be printed in the business cards is:
Company's name: Velmor Home Design
Company's Logo (attached)
My name: Noel Bramwit
Address, phone and email:
2715 N Parkline Road, Ste 348
Fernbrook, OR 97412
(470) 555 0187
nbramwit@velmordesign.example
Website: velmordesign.example

```html
<!DOCTYPE html>
<html lang="en">
<head>
<meta charset="utf-8">
<title>Velmor Home Design — Business Card</title>
<link rel="stylesheet" href="https://fonts.googleapis.com/css2?family=Montserrat:wght@400;500;600&display=swap">
<style>
  :root {
    --backdrop: #8a8a8a;
    --card-light: #f2f2f2;
    --card-dark: #050608;
    --ink: #111111;
    --paper: #ffffff;
  }
  html, body {
    margin: 0;
    padding: 0;
    width: 1200px;
    height: 1196px;
    overflow: hidden;
    background: var(--backdrop);
    font-family: "Montserrat", Arial, sans-serif;
  }
  .canvas {
    position: relative;
    width: 1200px;
    height: 1196px;
  }
  .card {
    position: absolute;
    left: 367px;
    width: 473px;
  }
  .card--front {
    top: 271px;
    height: 317px;
    background: var(--card-light);
    color: var(--ink);
  }
  .card--back {
    top: 610px;
    height: 318px;
    background: var(--card-dark);
    color: var(--paper);
  }
  .holder-name {
    position: absolute;
    left: 37px;
    top: 73px;
    margin: 0;
    font-size: 12px;
    line-height: 14px;
    font-weight: 600;
    letter-spacing: 0.14em;
    text-transform: uppercase;
  }
  .brand {
    position: absolute;
    right: 36px;
    top: 74px;
    display: flex;
    align-items: center;
    gap: 7px;
  }
  .brand__square {
    width: 22px;
    height: 22px;
    background: var(--ink);
  }
  .brand__divider {
    width: 1px;
    height: 24px;
    background: var(--ink);
    margin-left: 4px;
  }
  .brand__name {
    margin: 0;
    font-size: 7.8px;
    font-weight: 500;
    line-height: 8.6px;
    letter-spacing: 0.22em;
    text-transform: uppercase;
  }
  .contact {
    position: absolute;
    margin: 0;
    font-size: 9.3px;
    font-weight: 400;
    line-height: 11.2px;
    font-style: normal;
  }
  .contact--online { left: 37px; top: 157px; }
  .contact--phone  { left: 288px; top: 157px; }
  .contact--address { left: 37px; top: 217px; }
  .back-brand {
    position: absolute;
    left: 0;
    right: 0;
    top: 50%;
    transform: translateY(-50%);
    display: flex;
    flex-direction: column;
    align-items: center;
    gap: 14px;
  }
  .back-brand__square {
    width: 22px;
    height: 22px;
    border: 2.5px solid var(--paper);
    box-sizing: border-box;
  }
  .back-brand__name {
    margin: 0;
    font-size: 16px;
    font-weight: 500;
    letter-spacing: 0.3em;
    text-transform: uppercase;
    text-align: center;
    line-height: 1.5;
  }
</style>
</head>
<body>
<main class="canvas">
  <section class="card card--front" aria-label="Business card front">
    <h1 class="holder-name">Noel Bramwit</h1>
    <div class="brand">
      <span class="brand__square" aria-hidden="true"></span>
      <span class="brand__divider" aria-hidden="true"></span>
      <p class="brand__name">Velmor<br>Home<br>Design</p>
    </div>
    <p class="contact contact--online">nbramwit@velmordesign.example<br>velmordesign.example</p>
    <p class="contact contact--phone">(470) 555 0187</p>
    <address class="contact contact--address">2715 N Parkline Road, Ste 348<br>Fernbrook, OR 97412</address>
  </section>

  <section class="card card--back" aria-label="Business card back">
    <div class="back-brand">
      <span class="back-brand__square" aria-hidden="true"></span>
      <p class="back-brand__name">Velmor<br>Home Design</p>
    </div>
  </section>
</main>
</body>
</html>
```